Law Firm Website

We are a small California based law firm specializing in business, corporate and litigation matters. We need to have our website redesigned. We are looking for a new and fresh look for our site, keeping in mind that we are a law firm.
What we don't want:
**the traditional "gavel" and "scales of justice" look
**anything too crazy
What we do want:
**sophisticated yet modern and fresh corporate look and feel
**samples of websites we really like:
http://www.mtrhllp-example.com
http://www.orwenlatch-example.com/
we also like:
http://www.verdtolbain-example.com/
http://www.qh-example.com/
http://www.pembrost-example.com/
http://www.nvtr-example.com
http://www.rmqlaw-example.com/
The content will be whatever is currently on our website (www.halvencourtlaw-example.com). We will be selecting the winner based on originality and keeping the above requirements in mind. Please note that the photos that you use will be the ones that we will be using, so choose wisely because the photos will make a difference.
Target Market(s)
Corporate clients
Industry/Entity Type
Law Firm
Look and feel

```html
<!DOCTYPE html>
<html lang="en">
<head>
<meta charset="utf-8">
<title>Halvencourt Law Group, LLP</title>
<link href="https://fonts.googleapis.com/css2?family=Cinzel:wght@400;700&family=Noto+Serif&family=Roboto+Slab:wght@300;400&family=Open+Sans:wght@400;600&display=swap" rel="stylesheet">
<style>
  :root {
    --blue: #0a6fc2;
    --blue-light: #4a8fe0;
    --text: #555;
    --dark: #222;
    --nav: #9a9a9a;
    --rule: #dcdcdc;
    --footer-bg: #f5f5f5;
    --white: #fff;
  }
  * { margin: 0; padding: 0; box-sizing: border-box; }
  html, body { width: 1200px; height: 947px; overflow: hidden; background: var(--white); }
  body { position: relative; font-family: "Open Sans", sans-serif; color: var(--text); }

  .brand { position: absolute; left: 140px; top: 24px; display: flex; align-items: center; gap: 10px; }
  .brand-square { width: 83px; height: 83px; background: var(--blue-light); }
  .brand-name { font-family: "Noto Serif", serif; font-size: 16.5px; line-height: 21px; color: var(--blue); }

  .main-nav { position: absolute; top: 55px; left: 550px; font-family: "Roboto Slab", serif; font-weight: 300; font-size: 15px; }
  .main-nav a { position: absolute; color: var(--nav); text-decoration: none; white-space: nowrap; }

  .hero { position: absolute; left: 140px; top: 130px; width: 919px; height: 375px; overflow: hidden;
    background: linear-gradient(100deg, #e6e6e4 0%, #d8d8d6 45%, #aebfdc 62%, #6f8fd0 80%, #4d72c4 100%); }
  .hero-title { position: absolute; left: 565px; top: 72px; width: 340px; font-family: "Cinzel", serif; font-weight: 700;
    font-size: 40px; line-height: 46px; color: var(--white); }
  .hero-arrow { position: absolute; top: 172px; width: 41px; height: 41px; background: var(--white);
    display: flex; align-items: center; justify-content: center; }
  .hero-arrow.prev { left: 0; }
  .hero-arrow.next { right: 0; }
  .hero-dots { position: absolute; right: 0; bottom: 0; width: 145px; height: 27px; background: var(--white);
    border-radius: 14px 14px 0 0; display: flex; gap: 5px; justify-content: center; align-items: center; padding-bottom: 2px; }
  .hero-dots span { width: 11px; height: 11px; border-radius: 50%; background: #c8c8c8; }
  .hero-dots span.active { background: #2a8be0; }

  .column { position: absolute; top: 526px; width: 277px; }
  .col-welcome { left: 140px; width: 282px; }
  .col-practice { left: 461px; width: 300px; }
  .col-news { left: 781px; }
  .column h2 { font-family: "Cinzel", serif; font-weight: 700; font-size: 22px; color: var(--blue);
    padding-bottom: 4px; border-bottom: 1px solid var(--rule); margin-bottom: 22px; line-height: 30px; width: 277px; }
  .col-news h2 { width: 277px; }
  .column p { font-size: 12.5px; line-height: 20.6px; margin-bottom: 10px; }
  .more { font-size: 12.5px; color: var(--blue); text-decoration: none; display: inline-block; }

  .practice-list { list-style: none; margin: 15px 0 18px; }
  .practice-list li { font-size: 12.5px; line-height: 20.6px; color: var(--dark); padding-left: 14px; position: relative; }
  .practice-list li::before { content: "›"; position: absolute; left: 0; color: #888; }

  .news-item { display: flex; gap: 15px; padding: 4px 0 14px; border-bottom: 1px solid #e8e8e8; margin-bottom: 18px; }
  .news-item:last-of-type { border-bottom: none; margin-bottom: 0; padding-bottom: 10px; }
  .news-thumb { width: 73px; height: 74px; flex: none; border: 3px solid #e3e3e3; margin-top: 4px;
    background: linear-gradient(#f0f3f7, #c9d3de); }
  .news-date { font-size: 11px; color: #444; line-height: 16px; }
  .news-title { font-size: 13px; font-weight: 600; color: var(--blue); line-height: 21px; }
  .news-text { font-size: 12.5px; line-height: 20.6px; color: var(--text); }

  .site-footer { position: absolute; left: 0; top: 892px; width: 1200px; height: 55px; background: var(--footer-bg); }
  .footer-nav a { position: absolute; top: 20px; font-size: 13px; color: var(--dark); text-decoration: none; white-space: nowrap; }
  .copyright { position: absolute; right: 140px; top: 18px; font-size: 13px; color: #777; }
</style>
</head>
<body>
  <header>
    <div class="brand">
      <div class="brand-square"></div>
      <div class="brand-name">Halvencourt Law Group, LLP<br>Attorneys at Law</div>
    </div>
    <nav class="main-nav">
      <a style="left:0">Home</a>
      <a style="left:88px">About HLG</a>
      <a style="left:202px">Practice Areas</a>
      <a style="left:347px">Links</a>
      <a style="left:434px">Contact</a>
    </nav>
  </header>

  <section class="hero" role="img" aria-label="Photograph of a white marble government building with columns under a blue sky">
    <div class="hero-title">Lorem Ipsum is Simple dummy text</div>
    <div class="hero-arrow prev"><svg width="14" height="24" viewBox="0 0 14 24"><path d="M12 2 L3 12 L12 22" fill="none" stroke="#0a6fc2" stroke-width="3"/></svg></div>
    <div class="hero-arrow next"><svg width="14" height="24" viewBox="0 0 14 24"><path d="M2 2 L11 12 L2 22" fill="none" stroke="#0a6fc2" stroke-width="3"/></svg></div>
    <div class="hero-dots"><span class="active"></span><span></span><span></span><span></span><span></span><span></span></div>
  </section>

  <section class="column col-welcome">
    <h2>Welcome to HLG</h2>
    <p>Halvencourt Law Group, LLP provides quality legal representation to corporate as well as individual clients in the areas of business, corporate, securities, products liability, civil litigation (in State and Federal Courts), Alternative Dispute Resolution (arbitration and mediation), as well as a host of transactional matters.</p>
    <p>Our attorneys are committed to providing zealous advocacy in litigation, as well as creative approaches to difficult challenges that face our business clients. Our goal is to provide the</p>
    <a class="more">[ Read more.. ]</a>
  </section>

  <section class="column col-practice">
    <h2>Practice Areas</h2>
    <p>The key to your success is having the right team supporting you.&nbsp; Our attorneys can provide a key component: aggressive legal representation.&nbsp; We represent clients in a wide variety of fields, including:</p>
    <ul class="practice-list">
      <li>Civil Litigation</li>
      <li>Employment Law</li>
      <li>Arbitration</li>
      <li>Mediation</li>
      <li>Corporate Securities</li>
      <li>Corporate Governance</li>
    </ul>
    <a class="more">[ Read more.. ]</a>
  </section>

  <section class="column col-news">
    <h2>Latest News</h2>
    <article class="news-item">
      <div class="news-thumb" role="img" aria-label="Portrait of a businesswoman in a dark suit"></div>
      <div>
        <div class="news-date">07 Feb 2013</div>
        <div class="news-title">Lorem Ipsum</div>
        <div class="news-text">Lorem Ipsum is simply dummy text of the printing and typesetting industry.</div>
      </div>
    </article>
    <article class="news-item">
      <div class="news-thumb" role="img" aria-label="Portrait of a businesswoman in a dark suit"></div>
      <div>
        <div class="news-date">07 Feb 2013</div>
        <div class="news-title">Lorem Ipsum</div>
        <div class="news-text">Lorem Ipsum is simply dummy text of the printing and typesetting industry.</div>
      </div>
    </article>
    <a class="more">[ View All ]</a>
  </section>

  <footer class="site-footer">
    <nav class="footer-nav">
      <a style="left:140px">Home</a>
      <a style="left:212px">About HLG</a>
      <a style="left:305px">Practice Areas</a>
      <a style="left:419px">Links</a>
      <a style="left:485px">Contact</a>
    </nav>
    <div class="copyright">© 2014 Halvencourt Law Group. All Right Reserved</div>
  </footer>
</body>
</html>
```